Leading the way in online fitness and education requires power house web design

If you need to contact me you can do so via
skype: Travlin

We need a website designed for new company based in Houston Texas called "TravlinFit". We offer web based training and nutrition programs for our members for example we use the same software as these companies: http://marobelka.com/ http://www.liftquorra.com/ i would like my visitors to be captivated by the level of design creativity of the site.

colors to use would be grey, orange and green.
for example i like the green of this site http://www.cartbeam.com/
i will upload my logo files so you can get a feel for shades of grey and orange.

there is a 3d effect filter i would like applied to my logo for use in the web design i have uploaded what that effect looks like.

i will need your designs to be complete with all interior pages which will include Home, Fitness, Nutrition, Fit Lounge, Fit Score, Fit School, Contact Us, Sign up.

fit lounge on my site is the same as pathwick on liftquorra and locker room on marobelka just re branded.

fit school is a research corner for members to learn about health and fitness, we are members of major medical journals on health and fitness and will have all our articles be from the newest research findings.

competitor sites
these sites use same software:
http://marobelka.com/
http://www.liftquorra.com/

these sites are other software.
http://home.sprintmesa.com/software-for-athletes.aspx
http://www.vigordex.com/

here are some websites that i like:
http://www.crestwaveplay.com/
http://www.nub-lantern.com/
http://fimzol.com/
http://www.parqudo.com/
http://www.lortavi.de/fandiloop/
http://brisketmade.com/

i also like the greens in this site that i am uploading

I have been reviewing the designs and would like to update everyone at once I do not want a normal fitness website design style, no testimonials, blog post, bodyfat calculator

my website will be a membership based website. i want the website to sell the main points of my fitness app that my members will have access to look at the comments for my selling points, use those points in the site create designs and graphics to visualize those points.

look at these sites and gain inspiration

http://www.tuvelo.com.pl/#/projekty/case-studies
http://www.quendar.com/en#/home#ld-kpvm-402617-0045
http://www.nub-lantern.com/
http://fimzol.com/
http://www.parqudo.com/

i have a few designers asking me what the selling points are, the website needs to be built around these points

main selling points.

overview

programs utilize the best multi-joint exercises combined with high intensity cardio, to give you a full-body workout, efficiently and effectively. This means you’re burning more calories and building more lean muscle per unit of time than traditional weight training and cardio programs.

When you sign up, you''ll receive a work out and diet plan to fit your goals and fitness level. As you progress through your plan, you can use the personal fitness and meal calendar to record your results. When you sign-up we''ll ask you a series of questions and your workouts will be tailored to your exact needs. That means never having to use a generic diet and exercise plan again.

If you''ve ever tried to lose weight and build muscle and didn''t succeed, we feel your pain. Until now, trying to navigate all the fitness fads and latest trends on your own has been difficult. The best option - hiring a certified personal trainer - may be out of your financial reach. That''s where we come in - we''re personal trainers on a mission to help you reach your fitness goals quickly and for less money than in person training. Best of all, we''re here to help you day or night.

Fitness

Personal Fitness Calendar

Tailored to the member’s schedule and flexible to accommodate any changes to a member’s regular fitness schedule. Track your progress and stay on track with your fitness goals.

Custom Fitness Plan

Based on a member’s current physical condition and goals.

• Step by step exercise instructions
• 3-D video demonstrations of over 600 exercises, including functional and body-weight only movements
• Equipment filter can customize plans to your gym’s equipment package
• Record workouts to track exercise history and progression

Nutrition

Nutritional Assessment

Daily recommended caloric intake (Protein, Carbohydrates and Fats), based on personal profile and daily fitness plan.

Custom Meal Plan

Personalized meal plan based on nutritional assessment.

• Choose number of meals per day
• Add dietary restrictions, food preferences or dislikes
• Database of thousands of ingredients allows for hundreds of thousands of meal combinations
• Include favorite foods by entering custom nutritional information

Weight tracking

Calculate goal weight and track weight-loss or weight-gain progress. You will reach your goals in no time.

Fit Lounge

What is the most important part of any workout or fitness program? Staying motivated. And what better form of motivation than positive encouragement from your peers?

Fit Lounge is fitness focused social network for health-minded individuals looking for a simple and convenient place to track their workout goals and monitor their progress. A unique system of motivation, support and accountability makes setting fitness goals and then keeping up with them easy

Track

Start by setting fitness goals that you want to track. They can be anything from running and jogging to how many hours of sleep you are getting and how many glasses of water you are drinking every day. Other members of the travlinfits community might be tracking the same workout goals as you, so you can always join their groups as well.

Share

Once you start tracking your workout goals, you can share your progress with your friends. Reach a new max on your bench press? Let everyone know. Eclipse the 10 mile mark on your daily run? Spread the word! The communication of encouragement back and forth is a great way to ensure that everyone stays on track with their workout goals.

Achieve

Of course, the point of any workout or fitness program is to achieve the goals you’ve set. And with help from travlinfits workout tracking tools and encouragement from the community, you will achieve your workout goals in no time. When you see a friend has achieved his or her fitness goals, you can send them a virtual “fist bump” as a sign of congratulations. The number of “fist bumps” each user accumulates will be displayed on their profile, providing additional motivation and a healthy dose of competition.

Reason: i dont feel the designs i have received are of the quality i am looking for

check this website out, i know its flash, but i also know you can get creative without flash and have nice effects throughout the site.

http://www.driftlane-hub.com/

I dont want plain jane designs, insert the content i provided into the site and have it explored in a unique way. take as much time on the design as you need as i will keep extending deadline until i find one that is perfect.

as said before don't make the site anything like the competition sites, its only purpose is to sell the memberships using content provided so i need an innovative way to for them to explore that content,

as your designing this site add me on skype so i can detail and help brainstorm ideas my skype id is travlin
you can stray from the color scheme a little or throw it away if you want i just want to see how creative you can get.

Industry/Entity Type

School

Requirements
Nice to have
• if you notice at the bottom of http://marobelka.com/ she has the orange bar with the three short content parts, i like the idea of having a space like that for similar content.

on http://www.vigordex.com/ if you look to the left side of the scrolling icons i like the idea of having icons or animated pictures to point of key benefits.

```html
<!DOCTYPE html>
<html lang="en">
<head>
<meta charset="utf-8">
<title>TravlinFit – Home</title>
<link href="https://fonts.googleapis.com/css2?family=Roboto+Condensed:wght@400;700&family=Roboto:wght@400&display=swap" rel="stylesheet">
<style>
  :root{
    --orange:#f26a10;
    --orange-deep:#c9440a;
    --tile:#2e3538;
    --ink:#f2f2f2;
    --muted:#c9c9c9;
    --header:#d4d4d4;
    --brand:#3a3a3a;
    --black:#000;
    --button:#d9d9d9;
    --icon:#333;
  }
  *{box-sizing:border-box;margin:0;padding:0}
  html,body{width:1200px;height:720px;overflow:hidden;background:var(--black)}
  body{font-family:"Roboto Condensed",Arial,sans-serif;color:var(--ink);position:relative}

  .site-header{position:absolute;left:0;top:0;width:1200px;height:79px;background:var(--header);
    display:flex;align-items:center;justify-content:center;gap:12px}
  .brand-dot{width:34px;height:34px;border-radius:50%;background:var(--orange)}
  .brand-name{font-weight:700;font-size:44px;color:var(--brand);letter-spacing:.5px}

  .stage{position:absolute;left:0;top:79px;width:1200px;height:641px;overflow:hidden;
    background:
      radial-gradient(ellipse 260px 200px at 40px 300px, rgba(242,106,16,.95), rgba(201,68,10,.55) 45%, transparent 75%),
      radial-gradient(ellipse 340px 90px at 120px 560px, rgba(242,106,16,.85), transparent 70%),
      radial-gradient(ellipse 230px 230px at 1170px 250px, rgba(242,106,16,.95), rgba(201,68,10,.5) 45%, transparent 75%),
      radial-gradient(ellipse 300px 70px at 1050px 470px, rgba(242,106,16,.55), transparent 70%),
      var(--black)}

  .hero-photo{position:absolute;z-index:0;left:446px;top:4px;width:314px;height:440px;border-radius:50%;
    background:radial-gradient(ellipse at 50% 45%, #a5705a 0%, #7a4d3c 35%, #3a2d2c 65%, rgba(0,0,0,0) 100%)}

  .main-nav{position:absolute;z-index:3;top:24px;left:0;width:1200px;display:flex;justify-content:center;gap:8px;
    font-weight:700;font-size:14.5px;text-transform:uppercase;letter-spacing:.2px;white-space:nowrap}
  .main-nav a{color:var(--ink);text-decoration:none}
  .main-nav a.is-current{color:var(--orange)}
  .main-nav .sep{color:var(--ink)}
  .nav-rule{position:absolute;z-index:3;top:50px;left:270px;width:660px;height:2px;
    background:linear-gradient(90deg,transparent,#8a8a8a 20%,#bdbdbd 50%,#8a8a8a 80%,transparent)}

  .tile{position:absolute;z-index:2;height:46px;display:flex;align-items:center;white-space:nowrap;
    background:linear-gradient(to bottom,var(--orange) 0 2px,var(--tile) 2px calc(100% - 2px),var(--orange) calc(100% - 2px));
    font-weight:700;font-size:14px;letter-spacing:.5px;text-transform:uppercase;line-height:1.1}
  .tile--left{clip-path:polygon(8px 0,100% 0,calc(100% - 22px) 100%,0 100%);padding-left:66px}
  .tile--right{clip-path:polygon(0 0,calc(100% - 8px) 0,100% 100%,22px 100%);justify-content:flex-end;padding-right:66px;text-align:left}
  .tile .label{color:var(--ink)}
  .tile.is-accent .label{color:var(--orange)}
  .tile .dot{display:inline-block;width:7px;height:7px;border-radius:50%;background:var(--orange);margin:0 6px;vertical-align:middle}

  .icon-box{position:absolute;top:4px;width:50px;height:38px;background:#fff;
    display:flex;align-items:center;justify-content:center;clip-path:polygon(6px 0,100% 0,calc(100% - 6px) 100%,0 100%)}
  .tile--left .icon-box{left:8px;border-right:3px solid var(--orange)}
  .tile--right .icon-box{right:10px;border-left:3px solid var(--orange)}
  .icon-box.is-active{background:var(--orange)}
  .icon-box svg{width:22px;height:22px}

  .actions-rule{position:absolute;z-index:2;left:240px;width:720px;height:1px;background:linear-gradient(90deg,transparent,var(--orange),transparent)}
  .actions{position:absolute;z-index:2;top:462px;left:217px;display:flex;gap:9px}
  .actions a{width:186px;height:30px;display:flex;align-items:center;justify-content:center;
    background:var(--button);color:#1c1c1c;border:2px solid #f0f0f0;text-decoration:none;white-space:nowrap;
    font-weight:700;font-size:15.5px;text-transform:uppercase;letter-spacing:.3px}
  .actions a.is-current{background:var(--orange);color:#fff}

  .contact{position:absolute;z-index:2;top:511px;left:0;width:1200px;text-align:center}
  .contact .call{font-weight:700;font-size:16px;letter-spacing:.8px;color:var(--muted)}
  .contact .phone{font-weight:700;font-size:37px;letter-spacing:2px;color:#dcdcdc;margin-top:2px;line-height:1.1}
  .contact .address{font-family:Roboto,Arial,sans-serif;font-size:12.5px;color:var(--muted);margin-top:5px}
  .contact .copyright{font-family:Roboto,Arial,sans-serif;font-size:10px;color:var(--muted);margin-top:13px}
</style>
</head>
<body>
  <header class="site-header">
    <span class="brand-dot"></span>
    <span class="brand-name">TravlinFit</span>
  </header>

  <main class="stage">
    <div class="hero-photo" role="img" aria-label="Photo of a muscular athlete standing in front of a gym partner"></div>

    <nav class="main-nav">
      <a class="is-current" href="#">Home</a><span class="sep">|</span>
      <a href="#">Fitness</a><span class="sep">|</span>
      <a href="#">Nutrition</a><span class="sep">|</span>
      <a href="#">Fit Lounge</a><span class="sep">|</span>
      <a href="#">Fit Score</a><span class="sep">|</span>
      <a href="#">Fit School</a><span class="sep">|</span>
      <a href="#">Contact Us</a><span class="sep">|</span>
      <a href="#">Sign Up</a>
    </nav>
    <div class="nav-rule"></div>

    <div class="tile tile--left is-accent" style="left:263px;top:76px;width:233px">
      <span class="icon-box is-active"><svg viewBox="0 0 22 22"><circle cx="11" cy="11" r="6" fill="#fff"/></svg></span>
      <span class="label">Fitness<span class="dot"></span></span>
    </div>
    <div class="tile tile--left" style="left:248px;top:139px;width:219px">
      <span class="icon-box"><svg viewBox="0 0 22 22"><rect x="3" y="4" width="16" height="15" fill="none" stroke="#333" stroke-width="1.5"/><line x1="3" y1="8" x2="19" y2="8" stroke="#333" stroke-width="1.5"/></svg></span>
      <span class="label">Personal Fitness<br>Calendar</span>
    </div>
    <div class="tile tile--left" style="left:242px;top:203px;width:213px">
      <span class="icon-box"><svg viewBox="0 0 22 22"><circle cx="11" cy="11" r="6" fill="#333"/></svg></span>
      <span class="label">Custom Fitness<br>Plan</span>
    </div>
    <div class="tile tile--left is-accent" style="left:245px;top:268px;width:182px">
      <span class="icon-box"><svg viewBox="0 0 22 22"><circle cx="11" cy="11" r="6" fill="#333"/></svg></span>
      <span class="label">Fit Lounge<span class="dot"></span></span>
    </div>
    <div class="tile tile--left" style="left:258px;top:333px;width:187px">
      <span class="icon-box"><svg viewBox="0 0 22 22"><path d="M4 11h12M12 6l5 5-5 5" fill="none" stroke="#333" stroke-width="2"/></svg></span>
      <span class="label">Track</span>
    </div>
    <div class="tile tile--left" style="left:277px;top:396px;width:194px">
      <span class="icon-box"><svg viewBox="0 0 22 22"><circle cx="11" cy="6" r="2.5" fill="#333"/><circle cx="5" cy="16" r="2.5" fill="#333"/><circle cx="17" cy="16" r="2.5" fill="#333"/><path d="M11 6L5 16M11 6l6 10" stroke="#333" stroke-width="1.5"/></svg></span>
      <span class="label">Share</span>
    </div>

    <div class="tile tile--right is-accent" style="left:705px;top:76px;width:234px">
      <span class="label"><span class="dot"></span>Nutrition</span>
      <span class="icon-box"><svg viewBox="0 0 22 22"><circle cx="11" cy="12" r="6" fill="#333"/></svg></span>
    </div>
    <div class="tile tile--right" style="left:736px;top:139px;width:219px">
      <span class="label">Nutritional<br>Accessment</span>
      <span class="icon-box"><svg viewBox="0 0 22 22"><circle cx="11" cy="11" r="8" fill="none" stroke="#333" stroke-width="1.5"/></svg></span>
    </div>
    <div class="tile tile--right" style="left:769px;top:203px;width:190px">
      <span class="label">Custom Meal<br>Plan</span>
      <span class="icon-box"><svg viewBox="0 0 22 22"><circle cx="11" cy="12" r="6" fill="#333"/></svg></span>
    </div>
    <div class="tile tile--right" style="left:759px;top:268px;width:200px">
      <span class="label">Weight Tracking</span>
      <span class="icon-box"><svg viewBox="0 0 22 22"><circle cx="11" cy="11" r="8" fill="#777"/><circle cx="11" cy="11" r="5" fill="none" stroke="#fff" stroke-width="1.2"/></svg></span>
    </div>
    <div class="tile tile--right" style="left:757px;top:333px;width:186px">
      <span class="label">Balance</span>
      <span class="icon-box"><svg viewBox="0 0 22 22"><path d="M3 11h16" stroke="#333" stroke-width="2"/><circle cx="11" cy="11" r="3" fill="#333"/></svg></span>
    </div>
    <div class="tile tile--right" style="left:734px;top:396px;width:194px">
      <span class="label">Achieve</span>
      <span class="icon-box"><svg viewBox="0 0 22 22"><path d="M5 11l4 4 8-9" fill="none" stroke="#333" stroke-width="2"/></svg></span>
    </div>

    <div class="actions-rule" style="top:456px"></div>
    <nav class="actions">
      <a class="is-current" href="#">View Class Schedules</a>
      <a href="#">Sign Up For Class</a>
      <a href="#">View Our Calendar</a>
      <a href="#">Book A Party</a>
    </nav>
    <div class="actions-rule" style="top:497px"></div>

    <section class="contact">
      <p class="call">CALL US TODAY</p>
      <p class="phone">1.555.214.0376</p>
      <p class="address">48, Harlow St. Brenfield, Ohio 4402</p>
      <p class="copyright">Copyright © 2012. TravlinFit</p>
    </section>
  </main>
</body>
</html>
```